Spy/Espionage/Counterintelligence Membership Community Needs a PowerPoint Template

We need a powerpoint template for one of our business verticals focused on spies, espionage, and counterintelligence. The name of it is "Amber Harbor Guild" and the logo is attached. Amber Harbor Guild is a community that connects people with experts in espionage and counterintelligence through an online social network, as well as in-person events. We would like to see designs that incorporate the red and black of the logo. The design should communicate mystery/suspense and peak curiosity.

Target Market(s)

Late 20s to baby boomers, male

Industry/Entity Type

Social Club

Font styles to use
Sans Serif

Colors
ec1f27
000000
ffffff

Requirements
Must have
• A user-friendly ppt template file. Incorporate basic fonts that don't have to be installed on every computer for presentations. A cover slide and a basic inside slide. A white background. I will also need graphic source files.
Nice to have
• Plenty of space for slide title and body content. Logo on every slide.
Should not have
• Inconsistency with fonts. Misalignment of images.

```html
<!DOCTYPE html>
<html lang="en">
<head>
<meta charset="utf-8">
<title>Amber Harbor Guild – Content Slide</title>
<link href="https://fonts.googleapis.com/css2?family=Carlito:ital,wght@0,400;0,700;1,400&display=swap" rel="stylesheet">
<style>
  :root {
    --ink: #000000;
    --brand-red: #d10000;
    --bright-red: #ff0000;
    --muted-red: #c25b5a;
    --deep-red: #5e0000;
    --charcoal: #262626;
    --body-grey: #555555;
    --paper: #ffffff;
  }
  * { margin: 0; padding: 0; box-sizing: border-box; }
  html, body { width: 1200px; height: 900px; overflow: hidden; background: var(--paper); }
  body { font-family: "Carlito", Calibri, sans-serif; color: var(--ink); }

  .slide { position: relative; width: 1200px; height: 900px; background: var(--paper); overflow: hidden; }

  .slide-title { position: absolute; left: 38px; top: 38px; font-size: 62px; font-weight: 700; letter-spacing: 0.5px; }
  .slide-subtitle { position: absolute; left: 70px; top: 120px; font-size: 36px; font-weight: 700; color: var(--brand-red); }
  .slide-section { position: absolute; left: 111px; top: 177px; font-size: 24px; font-weight: 700; }

  .body-copy { position: absolute; left: 118px; top: 222px; width: 1010px; font-size: 18.6px; line-height: 25px; color: var(--body-grey); }
  .body-copy p + p { margin-top: 25px; }

  .block-label { position: absolute; font-size: 20px; color: var(--brand-red); }
  .label-list { left: 148px; top: 425px; }
  .label-bullets { left: 731px; top: 436px; }
  .label-palette { left: 938px; top: 435px; }

  .sample-list { position: absolute; left: 162px; top: 484px; list-style: none; font-size: 16.8px; font-style: italic; }
  .sample-list li { height: 35.2px; line-height: 20px; }

  .bullet-set { position: absolute; left: 735px; top: 485px; }

  .palette { position: absolute; left: 940px; top: 469px; display: grid; grid-template-columns: repeat(3, 62px); column-gap: 12px; row-gap: 21px; }
  .swatch { width: 62px; height: 62px; }
  .swatch-black { background: var(--ink); }
  .swatch-brand { background: var(--brand-red); }
  .swatch-bright { background: var(--bright-red); }
  .swatch-muted { background: var(--muted-red); }
  .swatch-deep { background: var(--deep-red); }
  .swatch-charcoal { background: var(--charcoal); }

  .footer { position: absolute; left: 0; top: 795px; width: 1200px; height: 105px; display: flex; }
  .footer-brand { width: 176px; height: 105px; background: var(--brand-red); display: flex; flex-direction: column; align-items: center; justify-content: center; gap: 6px; }
  .brand-dot { width: 46px; height: 46px; border-radius: 50%; background: var(--ink); }
  .brand-name { font-size: 16px; font-weight: 400; color: var(--ink); white-space: nowrap; }
  .footer-band { flex: 1; position: relative; background: linear-gradient(180deg, #2a2a2a 0%, #141414 100%); }
  .footer-caption { position: absolute; left: 0; right: 0; top: 31px; text-align: center; font-size: 31px; color: var(--brand-red); padding-right: 40px; }
</style>
</head>
<body>
<main class="slide">
  <h1 class="slide-title">THIS IS HEADER</h1>
  <h2 class="slide-subtitle">This is Sub Header</h2>
  <h3 class="slide-section">This is&nbsp; Sub Sub Header</h3>

  <div class="body-copy">
    <p>Lorem ipsum dolor sit amet, consectetur adipiscing elit. Donec ullamcorper fringilla justo, vitae dignissim risus pharetra eu. Phasellus interdum ante sit amet metus pretium, a scelerisque metus tempus. Proin tincidunt ante vitae dolor ultricies, sit amet tincidunt leo tincidunt. Duis est tellus, dictum convallis mauris non, tristique interdum ligula.</p>
    <p>Aenean vel dapibus enim. Vestibulum malesuada augue nec dolor finibus, quis eleifend orci fermentum. Sed ullamcorper urna facilisis ligula aliquet aliquam. Sed lobortis elit eget risus convallis consectetur. Nulla facilisi. Cum sociis natoque penatibus et magnis dis parturient montes, nascetur ridiculus mus.</p>
  </div>

  <div class="block-label label-list">List style</div>
  <ul class="sample-list">
    <li>Aenean vitae eros ut leo aliquet volutpat eu sed lacus.</li>
    <li>In eget metus pretium, mollis metus a, fermentum neque.</li>
    <li>Fusce ut ligula euismod, aliquam ipsum in, pretium ligula.</li>
    <li>Mauris varius nisl ac felis rutrum suscipit.</li>
    <li>Nulla porttitor sapien quis risus ornare commodo.</li>
  </ul>

  <div class="block-label label-bullets">Bullet Style</div>
  <svg class="bullet-set" width="80" height="170" viewBox="0 0 80 170" aria-label="Bullet styles">
    <defs>
      <symbol id="bullet-triangle" viewBox="0 0 20 20"><path d="M6 4 L15 10 L6 16 Z"/></symbol>
      <symbol id="bullet-chevron-disc" viewBox="0 0 20 20"><circle cx="10" cy="10" r="9"/><path d="M8 5.5 L12.5 10 L8 14.5" fill="none" stroke="#fff" stroke-width="2.6"/></symbol>
      <symbol id="bullet-check" viewBox="0 0 20 20"><path d="M14 4 H3 V17 H16 V11" fill="none" stroke="currentColor" stroke-width="2"/><path d="M6 9 L10 13 L18 3" fill="none" stroke="currentColor" stroke-width="2.4"/></symbol>
      <symbol id="bullet-target" viewBox="0 0 20 20"><circle cx="10" cy="10" r="7.5" fill="none" stroke="currentColor" stroke-width="2.4"/><circle cx="10" cy="10" r="3"/></symbol>
      <symbol id="bullet-double" viewBox="0 0 20 20"><path d="M4 5 L9 10 L4 15 M10 5 L15 10 L10 15" fill="none" stroke="currentColor" stroke-width="2"/></symbol>
    </defs>
    <g fill="#d10000" color="#d10000">
      <use href="#bullet-triangle" x="0" y="5" width="20" height="20"/>
      <use href="#bullet-chevron-disc" x="0" y="40" width="20" height="20"/>
      <use href="#bullet-check" x="0" y="76" width="20" height="20"/>
      <use href="#bullet-target" x="0" y="111" width="20" height="20"/>
      <use href="#bullet-double" x="0" y="147" width="20" height="20"/>
    </g>
    <g fill="#000" color="#000">
      <use href="#bullet-triangle" x="55" y="3" width="20" height="20"/>
      <use href="#bullet-chevron-disc" x="55" y="38" width="20" height="20"/>
      <use href="#bullet-check" x="55" y="72" width="20" height="20"/>
      <use href="#bullet-target" x="55" y="108" width="20" height="20"/>
      <use href="#bullet-double" x="55" y="142" width="20" height="20"/>
    </g>
  </svg>

  <div class="block-label label-palette">Color Palette</div>
  <div class="palette">
    <div class="swatch swatch-black"></div>
    <div class="swatch swatch-brand"></div>
    <div class="swatch swatch-bright"></div>
    <div class="swatch swatch-muted"></div>
    <div class="swatch swatch-deep"></div>
    <div class="swatch swatch-charcoal"></div>
  </div>

  <footer class="footer">
    <div class="footer-brand">
      <div class="brand-dot"></div>
      <div class="brand-name">Amber Harbor Guild</div>
    </div>
    <div class="footer-band" role="img" aria-label="Dark tiled texture band">
      <div class="footer-caption">This is content slide</div>
    </div>
  </footer>
</main>
</body>
</html>
```